Brightacre Preschool UI Design

**This has to be designed in landscape and NOT portrait :)
We need a user interface design for login screen we will have displayed at all times on our Tablixes in the reception area. These Tablixes will log our "Kinderquests" in and out using a login and password, and will sign them in for the day. This is a brand new, state-of-the-art 21st century learning environment. Our logo was made my a designer on artmarketly :)
We will have 2 main login screens:
one for admin
one for parents
I would like something fun and playful - and possibly "natural" looking as we are a Reggio Emilia inspired program (similar to Montessori).
Please visit our website to learn more about us:
www.Brightacre.example
I attached an example of the buttons/options we will need on the login screen - just don't think it looks great and want something more professional/sophisticated.
Thank you!
Industry/Entity Type
Landscape
Requirements
Must have
- landscape orientation

```html
<!DOCTYPE html>
<html lang="en">
<head>
<meta charset="utf-8">
<title>Brightacre Staff Login</title>
<link rel="stylesheet" href="https://fonts.googleapis.com/css2?family=Jost:wght@300;400;500;600;700&display=swap">
<style>
  :root {
    --teal: #56c1a9;
    --teal-dark: #4ab29b;
    --slate: #7d8a9c;
    --muted: #9aa4b2;
    --field-border: #dde1e6;
    --icon: #a9b2bd;
    --white: #ffffff;
    --ink: #222;
  }
  * { box-sizing: border-box; margin: 0; padding: 0; }
  html, body { width: 1200px; height: 900px; overflow: hidden; background: var(--white); }
  body { font-family: "Jost", sans-serif; position: relative; }

  .status-bar {
    position: absolute; top: 0; left: 0; width: 1200px; height: 23px;
    display: flex; align-items: center; justify-content: space-between;
    padding: 0 8px; font-size: 14px; z-index: 3;
  }
  .status-bar .carrier, .status-bar .clock { color: var(--white); }
  .status-bar .clock { position: absolute; left: 560px; font-weight: 500; }
  .status-bar .battery { color: var(--ink); display: flex; align-items: center; gap: 4px; }
  .battery-cell { width: 26px; height: 12px; border: 1px solid #555; border-radius: 3px; padding: 1px; }
  .battery-cell span { display: block; height: 100%; background: #3cc13b; border-radius: 1px; }

  .hero {
    position: absolute; top: 0; left: 0; width: 638px; height: 900px;
    background:
      radial-gradient(ellipse at 40% 6%, rgba(255,226,140,.95) 0%, rgba(240,214,150,.6) 22%, transparent 50%),
      radial-gradient(ellipse at 40% 48%, #c9b7a4 0%, #a79a88 30%, transparent 60%),
      radial-gradient(ellipse at 90% 60%, #7f9a6a 0%, transparent 40%),
      linear-gradient(180deg, #e9dcc0 0%, #c8c0ad 35%, #8c8a7c 65%, #6e665b 100%);
  }
  .hero-caption { position: absolute; left: 59px; bottom: 86px; color: var(--white); }
  .hero-title { font-size: 54px; font-weight: 700; letter-spacing: 1px; line-height: 1; }
  .hero-subtitle { font-size: 33px; font-weight: 300; margin-top: 12px; line-height: 1; }

  .login-panel { position: absolute; top: 0; left: 638px; width: 562px; height: 900px; }
  .brand {
    position: absolute; top: 178px; left: 0; width: 562px;
    display: flex; justify-content: center; align-items: center; gap: 12px;
    color: var(--teal); font-size: 30px; font-weight: 500;
  }
  .brand-dot { width: 34px; height: 34px; border-radius: 50%; background: var(--teal); }
  .panel-heading {
    position: absolute; top: 322px; left: 0; width: 562px; text-align: center;
    font-size: 28px; font-weight: 300; color: var(--slate);
  }
  .field {
    position: absolute; left: 117px; width: 327px; height: 56px;
    border: 1px solid var(--field-border); border-radius: 4px;
    display: flex; align-items: center; padding: 0 16px; gap: 14px;
    font-size: 17px; color: var(--muted); font-weight: 400;
  }
  .field svg { width: 20px; height: 20px; fill: var(--icon); flex: none; }
  .field .field-label { flex: 1; }
  .field-username { top: 404px; }
  .field-password { top: 484px; }
  .forgot-link { position: absolute; left: 117px; top: 580px; font-size: 17px; color: var(--muted); }
  .login-button {
    position: absolute; left: 281px; top: 564px; width: 163px; height: 56px;
    background: var(--teal); color: var(--white); border-radius: 3px;
    display: flex; align-items: center; justify-content: center;
    font-size: 16px; font-weight: 600; letter-spacing: .4px;
    box-shadow: 0 6px 14px rgba(86,193,169,.45);
  }
  .nav-link {
    position: absolute; top: 743px; display: flex; align-items: center; gap: 6px;
    font-size: 18px; color: var(--teal);
  }
  .nav-link svg { width: 22px; height: 22px; fill: var(--teal); }
  .nav-home { left: 117px; }
  .nav-parents { right: 118px; }
</style>
</head>
<body>
  <div class="status-bar">
    <span class="carrier">●●○○○ Draftly</span>
    <span class="clock">9:41 AM</span>
    <span class="battery">100% <span class="battery-cell"><span></span></span></span>
  </div>

  <section class="hero" role="img" aria-label="Photo of a laughing young child in a cap and plaid shirt sitting on a wooden bench with an open book, sunlit trees behind">
    <div class="hero-caption">
      <h1 class="hero-title">BRIGHTACRE</h1>
      <p class="hero-subtitle">Opening in january 2018</p>
    </div>
  </section>

  <main class="login-panel">
    <div class="brand"><span class="brand-dot"></span>Brightacre</div>
    <h2 class="panel-heading">Only for Brightacre Staff</h2>

    <div class="field field-username">
      <svg viewBox="0 0 20 20"><circle cx="10" cy="6" r="4.5"/><path d="M1 19c0-5 4-8 9-8s9 3 9 8z"/></svg>
      <span class="field-label">Username</span>
    </div>
    <div class="field field-password">
      <svg viewBox="0 0 20 20"><circle cx="14" cy="6" r="5"/><path d="M10 8 2 16v3h3v-2h2v-2h2l3-3z"/></svg>
      <span class="field-label">Password</span>
      <svg viewBox="0 0 20 20"><path d="M10 4C5 4 1.5 10 1.5 10S5 16 10 16s8.5-6 8.5-6S15 4 10 4zm0 9.5a3.5 3.5 0 1 1 0-7 3.5 3.5 0 0 1 0 7z"/><circle cx="10" cy="10" r="1.8"/></svg>
    </div>

    <span class="forgot-link">Forgot Password?</span>
    <span class="login-button">STAFF LOGIN</span>

    <span class="nav-link nav-home">
      <svg viewBox="0 0 20 20"><path d="M10 2 1 10h3v8h4.5v-5h3v5H16v-8h3z"/></svg>Go to Home
    </span>
    <span class="nav-link nav-parents">
      <svg viewBox="0 0 22 20"><circle cx="8" cy="6" r="4"/><path d="M0 18c0-4 3.5-6.5 8-6.5s8 2.5 8 6.5z"/><circle cx="16" cy="6" r="3"/><path d="M17 18h5c0-3.5-2.5-5.5-6-5.8 1 1.3 1 3.5 1 5.8z"/></svg>Parents Login
    </span>
  </main>
</body>
</html>
```